Ferncrest Dental, LLC business card project

Business card to be designed with current logo.
Dental office- please keep design of card that looks clean and professional.
Please include the following info:
Ferncrest Dental, LLC
Dr. Lorna Pettigrew
2871 Marlowe Street
Bethlehem, PA 18093
610-555-0193
ferncrestdental.office@examplemail.test
Hello everyone-
Reason: Just got back from overseas- will look at all designs and provide feedback. Thank you!
Reason: Polling my friends for the final selection-
thank you to all those that participated- so many talented designers!

```html
<!DOCTYPE html>
<html lang="en">
<head>
<meta charset="utf-8">
<title>Ferncrest Dental, LLC — Business Card</title>
<link rel="stylesheet" href="https://fonts.googleapis.com/css2?family=Arimo:wght@400&display=swap">
<style>
  :root {
    --backdrop: #ece6dd;
    --card-white: #ffffff;
    --green-deep: #639e45;
    --green-lime: #b1d234;
    --green-brand: #5d9a3a;
    --text-light: #ffffff;
    --shadow: 0 6px 18px rgba(60, 45, 25, 0.18);
  }
  * { box-sizing: border-box; margin: 0; padding: 0; }
  html, body {
    width: 1200px;
    height: 900px;
    overflow: hidden;
    background: var(--backdrop);
    font-family: "Arimo", Arial, sans-serif;
  }
  .canvas {
    width: 1200px;
    height: 900px;
    display: flex;
    align-items: center;
    justify-content: center;
    gap: 48px;
  }
  .card {
    width: 520px;
    height: 320px;
    box-shadow: var(--shadow);
    position: relative;
    overflow: hidden;
  }
  /* Front */
  .card-front {
    background: var(--card-white);
    display: flex;
    align-items: center;
    justify-content: center;
  }
  .brand {
    display: flex;
    align-items: center;
    gap: 14px;
    color: var(--green-brand);
    font-size: 38px;
    font-weight: 400;
    letter-spacing: -0.5px;
  }
  .brand-dot {
    width: 22px;
    height: 22px;
    border-radius: 50%;
    background: var(--green-lime);
    flex: none;
  }
  /* Back */
  .card-back { display: flex; flex-direction: column; color: var(--text-light); }
  .back-top {
    background: var(--green-deep);
    height: 212px;
    display: flex;
    flex-direction: column;
    align-items: center;
  }
  .doctor-name {
    font-size: 40px;
    font-weight: 400;
    margin-top: 80px;
    letter-spacing: 0.2px;
  }
  .email {
    font-size: 15px;
    margin-top: 42px;
    letter-spacing: 0.2px;
  }
  .back-bottom {
    background: var(--green-lime);
    flex: 1;
    display: flex;
    align-items: center;
    justify-content: space-between;
    padding: 0 60px 8px 70px;
    font-size: 16px;
    line-height: 19px;
  }
  .phone-block { text-align: center; }
</style>
</head>
<body>
  <main class="canvas">
    <section class="card card-front" aria-label="Card front">
      <div class="brand">
        <span class="brand-dot" aria-hidden="true"></span>
        <span class="brand-name">Ferncrest Dental, LLC</span>
      </div>
    </section>

    <section class="card card-back" aria-label="Card back">
      <div class="back-top">
        <h1 class="doctor-name">Dr. Lorna Pettigrew</h1>
        <p class="email">ferncrestdental.office@examplemail.test</p>
      </div>
      <div class="back-bottom">
        <address class="address" style="font-style: normal;">
          2871 Marlowe Street<br>
          Bethlehem, PA 18093
        </address>
        <p class="phone-block">
          Call us at:<br>
          (610) 555-0193
        </p>
      </div>
    </section>
  </main>
</body>
</html>
```